TOVER - VAN SIGANGE DESIGN NEEDED

We have a van that needs signage on all sided .

We are TOVER Electrical. Logo is attached. Logo must be used on the Van design. We are looking for something that Will have presents on the road and stand out.

Please use the colours of the the Logo in your design.

Please also add the below:

Website: www.toverelectrical.com.au
Ph: 13 Tove (13 86 37)

Also add our slogan: Quality, reliability and Customer First

Service we do that can be added to the design are :

- Electrcial
- Led Lighting
- Solar Power
- CCTV

All customer

Solar

Must have
• Logo
• Van mock up must be used to show your design
Nice to have
• Service we ofer
Should not have
• No Extra added pictures. Please stick to the logo and colours.

```html
<!DOCTYPE html>
<html lang="en">
<head>
<meta charset="utf-8">
<title>TOVER Electrical – Van Signage</title>
<link href="https://fonts.googleapis.com/css2?family=Mukta:wght@600;700;800&display=swap" rel="stylesheet">
<style>
  :root {
    --ink: #25242c;
    --night: #0f1018;
    --red: #c8141e;
    --red-deep: #8e0d14;
    --paper: #ffffff;
    --light: #eef0f4;
  }
  html, body {
    margin: 0;
    padding: 0;
    width: 1200px;
    height: 940px;
    overflow: hidden;
    background: var(--paper);
  }
  .signage {
    position: relative;
    width: 1200px;
    height: 940px;
    font-family: "Mukta", sans-serif;
    color: var(--ink);
  }
  .wrap-graphics {
    position: absolute;
    inset: 0;
  }
  .services {
    position: absolute;
    left: 488px;
    top: 318px;
    width: 200px;
    margin: 0;
    padding: 0;
    list-style: none;
    text-align: center;
    font-weight: 700;
    font-size: 26px;
    line-height: 25px;
    letter-spacing: 0.2px;
    text-transform: uppercase;
  }
  .brand {
    position: absolute;
    left: 770px;
    top: 282px;
    width: 280px;
    text-align: center;
    color: var(--ink);
    font-weight: 800;
    line-height: 1;
  }
  .brand-name {
    display: block;
    font-size: 76px;
    letter-spacing: 1px;
  }
  .brand-trade {
    display: block;
    font-size: 14px;
    letter-spacing: 17px;
    margin-top: -4px;
    padding-left: 17px;
  }
  .slogan {
    position: absolute;
    left: 746px;
    top: 388px;
    width: 310px;
    margin: 0;
    text-align: center;
    font-weight: 700;
    font-size: 15px;
    color: var(--red);
    text-transform: uppercase;
    letter-spacing: 0.1px;
  }
  .contact {
    position: absolute;
    left: 396px;
    top: 538px;
    width: 370px;
    text-align: center;
    color: var(--paper);
  }
  .phone {
    display: flex;
    align-items: center;
    justify-content: center;
    gap: 8px;
    font-weight: 700;
    font-size: 31px;
    line-height: 1;
    letter-spacing: 0.3px;
  }
  .phone-icon {
    width: 24px;
    height: 24px;
  }
  .website {
    display: block;
    margin-top: 10px;
    font-weight: 600;
    font-size: 24px;
    line-height: 1;
    letter-spacing: 0.6px;
    text-transform: uppercase;
  }
</style>
</head>
<body>
<main class="signage">
  <svg class="wrap-graphics" width="1200" height="940" viewBox="0 0 1200 940" aria-hidden="true">
    <defs>
      <linearGradient id="swoosh-red" x1="0" y1="0" x2="1" y2="0">
        <stop offset="0" stop-color="var(--red-deep)"/>
        <stop offset="0.5" stop-color="var(--red)"/>
        <stop offset="1" stop-color="var(--red-deep)"/>
      </linearGradient>
    </defs>
    <!-- lower dark band -->
    <path class="band-dark" fill="var(--night)"
      d="M70 575 L364 575 C560 515 820 462 1100 452 L1100 600 L780 600 L780 620 L380 620 L380 608 L70 608 Z"/>
    <!-- white gap line -->
    <path class="band-gap" fill="var(--paper)"
      d="M364 562 C560 500 820 452 1100 440 L1100 452 C820 462 560 515 364 575 Z"/>
    <!-- red swoosh -->
    <path class="band-red" fill="url(#swoosh-red)"
      d="M364 545 C560 482 820 430 1100 418 L1100 440 C820 452 560 500 364 562 Z"/>
    <!-- front stripes -->
    <rect class="front-red" x="70" y="565" width="140" height="4" fill="var(--red)"/>
    <rect class="front-gap" x="70" y="569" width="140" height="6" fill="var(--light)"/>
    <!-- upper red accent line -->
    <path class="accent-line" fill="none" stroke="var(--red)" stroke-width="3"
      d="M800 418 C900 414 1000 412 1100 410"/>
  </svg>

  <ul class="services">
    <li>Electrcial</li>
    <li>LED Lighting</li>
    <li>Solar Power</li>
    <li>CCTV</li>
  </ul>

  <div class="brand">
    <span class="brand-name">TOVER</span>
    <span class="brand-trade">ELECTRICAL</span>
  </div>

  <p class="slogan">Quality, reliability and customer first</p>

  <div class="contact">
    <div class="phone">
      <svg class="phone-icon" viewBox="0 0 24 24" aria-hidden="true">
        <circle cx="12" cy="12" r="12" fill="var(--paper)"/>
        <path fill="var(--night)" d="M9.2 6.2c.4-.3 1-.2 1.2.3l1 2.1c.2.4.1.8-.2 1.1l-.9.8c.5 1.3 1.4 2.4 2.6 3.1l.9-.8c.3-.3.8-.3 1.1-.1l2 1.2c.4.3.5.8.2 1.2l-.9 1.2c-.4.5-1.1.7-1.7.5-3.3-1.1-5.7-3.8-6.5-7.2-.1-.6.1-1.2.6-1.6z"/>
      </svg>
      <span>13 TOVE (13 86 37)</span>
    </div>
    <span class="website">www.toverelectrical.com.au</span>
  </div>
</main>
</body>
</html>
```